Digital Album Cover - Quiet Frost (Candles Burning)

HiI need a digital album cover for a piano instrumental cover single

Artist: Toby Halvern
Title: Quiet Frost (Candles Burning)

The song was originally by Carl Dupree

Please use my logo

You can listen to the track herehttps://soundcloud.com/tobyhalvernpianist/quiet-frost-candles-burning-piano-instrumental-cover

Requirements
Must have
• My logo design Toby Halvern

```html
<!DOCTYPE html>
<html lang="en">
<head>
<meta charset="utf-8">
<title>Quiet Frost (Candles Burning) — Toby Halvern</title>
<link rel="stylesheet" href="https://fonts.googleapis.com/css2?family=Oswald:wght@300;500&display=swap">
<style>
  :root {
    --page-bg: #f4f1f1;
    --petal-light: #f6eef0;
    --petal-mid: #e9c6cc;
    --petal-rose: #d59aa3;
    --petal-deep: #9e4f5c;
    --title-pink: #c98790;
    --logo-ink: #2b2526;
    --tagline-ink: #4a3f41;
  }
  * { margin: 0; padding: 0; box-sizing: border-box; }
  html, body {
    width: 1200px;
    height: 900px;
    overflow: hidden;
    background: var(--page-bg);
  }
  .canvas {
    width: 1200px;
    height: 900px;
    display: flex;
    align-items: center;
    justify-content: center;
  }
  .album-cover {
    position: relative;
    width: 780px;
    height: 780px;
    overflow: hidden;
    box-shadow: 0 10px 30px rgba(80, 40, 50, 0.18);
  }
  .cover-photo {
    position: absolute;
    inset: 0;
    background:
      radial-gradient(ellipse 70% 55% at 65% 70%, var(--petal-mid) 0%, transparent 70%),
      radial-gradient(ellipse 60% 50% at 10% 95%, var(--petal-deep) 0%, transparent 70%),
      radial-gradient(ellipse 50% 40% at 100% 100%, var(--petal-rose) 0%, transparent 75%),
      linear-gradient(170deg, var(--petal-light) 0%, var(--petal-light) 30%, var(--petal-mid) 62%, var(--petal-rose) 85%, var(--petal-deep) 100%);
  }
  .cover-text {
    position: absolute;
    left: 43%;
    top: 10%;
    font-family: "Oswald", "Arial Narrow", sans-serif;
  }
  .album-title {
    font-weight: 300;
    color: var(--title-pink);
    text-transform: uppercase;
    line-height: 1.08;
  }
  .album-title .title-main {
    display: block;
    font-size: 64px;
    letter-spacing: 3px;
  }
  .album-title .title-sub {
    display: block;
    font-size: 30px;
    letter-spacing: 9px;
  }
  .artist-mark {
    display: flex;
    align-items: center;
    gap: 12px;
    margin-top: 34px;
    margin-left: -20px;
  }
  .artist-mark .mark-dot {
    width: 50px;
    height: 50px;
    border-radius: 50%;
    background: var(--logo-ink);
    flex-shrink: 0;
  }
  .artist-name {
    font-weight: 500;
    font-size: 30px;
    letter-spacing: 1px;
    color: var(--logo-ink);
    text-transform: uppercase;
    line-height: 1;
  }
  .artist-tagline {
    font-weight: 300;
    font-size: 14px;
    color: var(--tagline-ink);
    margin-top: 5px;
    letter-spacing: 0.5px;
  }
</style>
</head>
<body>
  <main class="canvas">
    <section class="album-cover">
      <div class="cover-photo" role="img" aria-label="Close-up photograph of soft pink flower petals under a faint geometric diamond overlay"></div>
      <div class="cover-text">
        <h1 class="album-title">
          <span class="title-main">Quiet Frost</span>
          <span class="title-sub">(Candles Burning)</span>
        </h1>
        <div class="artist-mark">
          <span class="mark-dot"></span>
          <div>
            <p class="artist-name">Toby Halvern</p>
            <p class="artist-tagline">Wedding &amp; Event Pianist</p>
          </div>
        </div>
      </div>
    </section>
  </main>
</body>
</html>
```